Partial Wrap Design for Painting Company

Need a wrap design that we can adapt to several vans. The immediate need is for 2016 Harlow KT300 and 2009 Brandt M-340. Vehicles are white.
We want a PARTIAL wrap (not full coverage).
We want to show;
- our phone number; (927) 555-LARK
- our website address; www.larkpainting.example
- our services; Interior - Exterior - Cabinet
Any questions? Feel free to ask.

Target Market(s)

Homeowners

Industry/Entity Type

Painting

```html
<!DOCTYPE html>
<html lang="en">
<head>
<meta charset="utf-8">
<title>Lark Painting – Partial Van Wrap</title>
<link href="https://fonts.googleapis.com/css2?family=Montserrat:ital,wght@0,500;0,800;1,700;1,800&display=swap" rel="stylesheet">
<style>
  :root{
    --bg:#f3f3f3;
    --body:#ffffff;
    --edge:#d9d9d9;
    --green:#9bc23c;
    --red:#d6363a;
    --orange:#e38b25;
    --blue:#4aa3d3;
    --ink:#333333;
  }
  html,body{margin:0;padding:0;width:1200px;height:2767px;overflow:hidden;background:var(--bg);}
  .canvas{position:relative;width:1200px;height:2767px;font-family:"Montserrat",sans-serif;color:var(--ink);}
  .wrap-panel{position:absolute;background:var(--body);border:2px solid var(--edge);border-radius:28px;overflow:hidden;}
  .wrap-panel svg{position:absolute;inset:0;width:100%;height:100%;}
  .brand{position:absolute;text-align:center;}
  .brand-name{display:block;font-weight:800;color:var(--red);line-height:1;letter-spacing:4px;}
  .brand-line{display:flex;align-items:center;justify-content:center;gap:12px;font-weight:500;letter-spacing:14px;color:var(--ink);}
  .brand-line::before,.brand-line::after{content:"";display:block;width:30px;height:2px;background:var(--ink);}
  .services{position:absolute;background:var(--ink);color:#fff;border-radius:6px;font-style:italic;font-weight:800;font-size:22px;height:34px;line-height:34px;text-align:center;letter-spacing:.5px;white-space:nowrap;}
  .contact{position:absolute;font-style:italic;white-space:nowrap;}
  .contact-phone{display:block;font-weight:800;font-size:29px;line-height:1.1;}
  .contact-web{display:block;font-weight:700;font-size:18px;}
</style>
</head>
<body>
<main class="canvas">

  <!-- Driver side -->
  <section class="wrap-panel side-driver" style="left:40px;top:60px;width:1120px;height:340px;">
    <svg viewBox="0 0 1120 340" preserveAspectRatio="none" aria-hidden="true">
      <path fill="var(--green)" d="M340 0H780C700 40 600 60 520 110C470 140 420 125 400 90C380 60 350 30 340 0Z"/>
      <path fill="var(--orange)" d="M430 340C450 270 520 250 620 250C720 250 770 285 830 340Z"/>
      <path fill="var(--orange)" d="M1010 40C1040 35 1070 50 1080 70V250C1040 235 1010 200 1030 150C1050 110 990 70 1010 40Z"/>
      <path fill="var(--red)" d="M990 340C1000 300 1040 275 1080 250V340Z"/>
    </svg>
  </section>
  <div class="brand" style="left:640px;top:95px;width:360px;">
    <span class="brand-name" style="font-size:104px;">LARK</span>
    <span class="brand-line" style="font-size:26px;margin-top:8px;">PAINTING</span>
  </div>
  <div class="services" style="left:620px;top:254px;width:440px;">INTERIOR &nbsp;|&nbsp; EXTERIOR &nbsp;|&nbsp; CABINET</div>
  <div class="contact" style="left:215px;top:245px;">
    <span class="contact-phone">(927) 555-LARK</span>
    <span class="contact-web">larkpainting.example</span>
  </div>

  <!-- Passenger side -->
  <section class="wrap-panel side-passenger" style="left:40px;top:600px;width:1120px;height:340px;">
    <svg viewBox="0 0 1120 340" preserveAspectRatio="none" aria-hidden="true">
      <path fill="var(--blue)" d="M40 40C60 20 90 20 110 60C130 100 140 130 120 160C100 190 60 170 40 170Z"/>
      <path fill="var(--red)" d="M40 190C90 210 140 260 150 340H40Z"/>
      <path fill="var(--green)" d="M320 0H780V70C700 90 660 110 600 100C520 90 480 40 420 25C380 15 340 10 320 0Z"/>
      <path fill="var(--orange)" d="M330 340C340 280 400 250 470 250C560 250 620 290 690 340Z"/>
    </svg>
  </section>
  <div class="brand" style="left:180px;top:630px;width:360px;">
    <span class="brand-name" style="font-size:104px;">LARK</span>
    <span class="brand-line" style="font-size:26px;margin-top:8px;">PAINTING</span>
  </div>
  <div class="services" style="left:143px;top:792px;width:440px;">INTERIOR &nbsp;|&nbsp; EXTERIOR &nbsp;|&nbsp; CABINET</div>
  <div class="contact" style="left:745px;top:785px;">
    <span class="contact-phone">(927) 555-LARK</span>
    <span class="contact-web">larkpainting.example</span>
  </div>

  <!-- Rear doors -->
  <section class="wrap-panel rear" style="left:280px;top:1165px;width:640px;height:470px;">
    <svg viewBox="0 0 640 470" preserveAspectRatio="none" aria-hidden="true">
      <path fill="var(--green)" d="M50 0H330C270 40 200 60 140 80C100 90 60 70 50 40Z"/>
      <path fill="var(--orange)" d="M0 110C30 90 60 100 70 150C80 200 70 250 90 290C105 320 70 345 0 340Z"/>
      <path fill="var(--red)" d="M0 350C60 350 120 380 160 470H0Z"/>
      <path fill="var(--blue)" d="M640 40C590 40 560 70 560 120C560 170 520 200 530 230C540 260 600 270 640 250Z"/>
      <path fill="var(--red)" d="M640 300C580 330 500 400 440 470H640Z"/>
    </svg>
  </section>
  <div class="brand" style="left:420px;top:1235px;width:360px;">
    <span class="brand-name" style="font-size:100px;">LARK</span>
    <span class="brand-line" style="font-size:26px;margin-top:10px;">PAINTING</span>
  </div>
  <div class="services" style="left:380px;top:1402px;width:440px;">INTERIOR &nbsp;|&nbsp; EXTERIOR &nbsp;|&nbsp; CABINET</div>
  <div class="contact" style="left:475px;top:1565px;text-align:center;width:250px;">
    <span class="contact-phone">(927) 555-LARK</span>
    <span class="contact-web">larkpainting.example</span>
  </div>

  <!-- Front hood -->
  <section class="wrap-panel front-hood" style="left:300px;top:2150px;width:600px;height:130px;border-radius:40px 40px 16px 16px;">
    <svg viewBox="0 0 600 130" preserveAspectRatio="none" aria-hidden="true">
      <path fill="var(--green)" d="M0 0H130C110 30 80 50 40 60C20 65 0 60 0 50Z"/>
      <path fill="var(--red)" d="M600 0H460C470 30 510 50 560 50C580 50 600 40 600 30Z"/>
    </svg>
  </section>
  <div class="brand" style="left:480px;top:2168px;width:240px;">
    <span class="brand-name" style="font-size:30px;letter-spacing:2px;">LARK</span>
    <span class="brand-line" style="font-size:9px;letter-spacing:8px;gap:6px;margin-top:2px;">PAINTING</span>
  </div>

  <!-- Front grille strip -->
  <section class="wrap-panel front-grille" style="left:340px;top:2330px;width:540px;height:100px;border-radius:10px;">
    <svg viewBox="0 0 540 100" preserveAspectRatio="none" aria-hidden="true">
      <path fill="var(--orange)" d="M0 100V40C40 20 100 15 140 40V100Z"/>
      <path fill="var(--blue)" d="M360 100C360 40 400 0 470 0H540V100Z"/>
    </svg>
  </section>

</main>
</body>
</html>
```